Corvane Business Cards & Staionary
Corvane, Inc.
Project: Corvane Business Cards & Staionary
Corvane Business Cards & Staionary - Real Estate
Creative Brief
Professional
Leonard T. Haskovich
President
418 W. Thornberry Blvd. Ashmere, TX 75412
len@corvanetx.com

```html
<!DOCTYPE html>
<html lang="en">
<head>
<meta charset="utf-8">
<title>Corvane, Inc. — Business Cards</title>
<link rel="stylesheet" href="https://fonts.googleapis.com/css2?family=Cormorant+Garamond:wght@500;600;700&display=swap">
<style>
  :root{
    --stage:#ececec;
    --paper:#ffffff;
    --gold-light:#e7b84a;
    --gold:#cf9622;
    --gold-deep:#a8721a;
    --ink:#3a3a3a;
    --slate:#5f5f5f;
    --swoosh:#8a8a8a;
    --on-gold:#ffffff;
  }
  *{margin:0;padding:0;box-sizing:border-box}
  html,body{width:1200px;height:874px;overflow:hidden;background:var(--stage)}
  body{position:relative;font-family:"Cormorant Garamond",Georgia,serif}

  .card{
    position:absolute;width:560px;height:320px;border-radius:22px;overflow:hidden;
    box-shadow:0 14px 30px rgba(0,0,0,.18);
  }

  /* back side */
  .card--back{
    left:580px;top:90px;
    background:radial-gradient(ellipse at 40% 30%,var(--gold-light),var(--gold) 55%,var(--gold-deep));
  }
  .back-mark{
    position:absolute;left:0;right:0;top:108px;text-align:center;
    color:var(--on-gold);font-size:54px;font-weight:600;letter-spacing:2px;
  }
  .back-web{
    position:absolute;left:0;right:0;top:214px;text-align:center;
    color:var(--on-gold);font-size:15px;letter-spacing:4px;text-transform:uppercase;
  }

  /* front side */
  .card--front{left:60px;top:460px;background:var(--paper)}
  .front-panel{position:absolute;inset:0}
  .brand{position:absolute;left:30px;top:112px;width:220px;text-align:center}
  .brand-square{display:block;width:30px;height:30px;margin:0 auto 10px;background:var(--gold)}
  .brand-name{color:var(--slate);font-size:40px;font-weight:600;line-height:1}
  .brand-tagline{margin-top:6px;color:var(--slate);font-size:9px;letter-spacing:1px;text-transform:uppercase}

  .person{position:absolute;left:300px;top:42px;color:var(--on-gold)}
  .person-name{font-size:19px;font-weight:600;letter-spacing:1px;font-variant:small-caps}
  .person-title{font-size:14px;letter-spacing:2px;text-transform:uppercase;margin-top:2px}

  .contact{position:absolute;left:300px;top:150px;list-style:none;color:var(--on-gold);font-size:13px;line-height:19px}
  .contact li{display:flex;align-items:center;gap:7px}
  .contact .ico{width:11px;height:11px;flex:none}
  .contact .indent{padding-left:18px}
</style>
</head>
<body>

  <section class="card card--back" aria-label="Card back">
    <div class="back-mark">Corvane</div>
    <div class="back-web">www.corvanetx.com</div>
  </section>

  <section class="card card--front" aria-label="Card front">
    <svg class="front-panel" width="560" height="320" viewBox="0 0 560 320" aria-hidden="true">
      <defs>
        <radialGradient id="goldPanel" cx="60%" cy="35%" r="75%">
          <stop offset="0" stop-color="#e7b84a"/>
          <stop offset=".55" stop-color="#cf9622"/>
          <stop offset="1" stop-color="#a8721a"/>
        </radialGradient>
      </defs>
      <path d="M262 0 C300 80 300 240 262 320 L282 320 C320 240 320 80 282 0 Z" fill="#8a8a8a"/>
      <path d="M280 0 C318 80 318 240 280 320 L560 320 L560 0 Z" fill="url(#goldPanel)"/>
    </svg>

    <div class="brand">
      <span class="brand-square"></span>
      <div class="brand-name">Corvane, Inc.</div>
      <div class="brand-tagline">Residential Sales and Property Management</div>
    </div>

    <div class="person">
      <div class="person-name">Leonard T. Haskovich</div>
      <div class="person-title">President</div>
    </div>

    <ul class="contact">
      <li><svg class="ico" viewBox="0 0 12 12"><path d="M6 1a3.5 3.5 0 0 0-3.5 3.5C2.5 7.5 6 11 6 11s3.5-3.5 3.5-6.5A3.5 3.5 0 0 0 6 1z" fill="#fff"/></svg>418 W. Thornberry Blvd.</li>
      <li class="indent">Ashmere, TX 75412</li>
      <li><svg class="ico" viewBox="0 0 12 12"><circle cx="6" cy="6" r="5.5" fill="#fff"/></svg>(555) 014-2290</li>
      <li><svg class="ico" viewBox="0 0 12 12"><circle cx="6" cy="6" r="5.5" fill="#fff"/></svg>(555) 014-7713</li>
      <li><svg class="ico" viewBox="0 0 12 12"><circle cx="6" cy="6" r="5.5" fill="#fff"/></svg>len@corvanetx.com</li>
      <li><svg class="ico" viewBox="0 0 12 12"><circle cx="6" cy="6" r="5.5" fill="#fff"/></svg>www.corvanetx.com</li>
    </ul>
  </section>

</body>
</html>
```